Pharmacy

Two sided postcard. Pictures on one side. Description on the other. We design and build pharmacies. pictures are some of our finished work. You can use as many pictures as you like not necessary to use all of them. Size of card should be 5"x7". See my website at display@brightfieldfixtures.com for more inspiration. I include the back of one card that I used recently. Both sids need design input. Feel free to contact me with questions.
Requirements
Must have
- Must be a two sided postcard
Nice to have
- I am sending a design of a sleek type postcard that I saw online as an example.
- https://lnk.example-pics.net/images/q7KmRz
- I am looking for something modern.
- Not limited to colors on my website.

```html
<!DOCTYPE html>
<html lang="en">
<head>
<meta charset="utf-8">
<title>Brightfield Fixtures &amp; Display Co Inc. – Postcard</title>
<link rel="stylesheet" href="https://fonts.googleapis.com/css2?family=Cinzel:wght@600;700&family=Nunito:ital,wght@0,400;0,700;1,400&display=swap">
<style>
  :root {
    --page: #3a3a3c;
    --cream: #f8f2e0;
    --red: #8c161c;
    --red-mid: #7a1218;
    --red-dark: #560508;
    --red-deep: #420305;
    --white: #ffffff;
  }
  html, body {
    margin: 0; padding: 0;
    width: 1162px; height: 1200px;
    overflow: hidden;
    background: var(--page);
  }
  .postcard {
    position: absolute;
    left: 186px;
    width: 790px; height: 564px;
    background: var(--cream);
    overflow: hidden;
  }
  .postcard--front { top: 24px; }
  .postcard--back { top: 612px; }
  .postcard svg { display: block; }

  .brand-title {
    font-family: "Cinzel", serif;
    font-weight: 700;
    color: var(--white);
    letter-spacing: 0.5px;
  }
  .front-title {
    position: absolute; left: 0; right: 0; bottom: 38px;
    text-align: center; font-size: 25px;
  }
  .back-header {
    position: absolute; left: 0; top: 0; width: 100%; height: 83px;
    background: var(--red);
  }
  .back-header .brand-title {
    position: absolute; left: 0; right: 0; top: 38px;
    text-align: center; font-size: 25px;
  }
  .back-footer {
    position: absolute; left: 0; bottom: 0; width: 100%; height: 33px;
    background: var(--red);
  }
  .about-panel {
    position: absolute; left: 0; top: 104px; width: 388px; height: 398px;
    background: var(--red-mid);
    font-family: "Nunito", sans-serif;
    color: var(--white);
  }
  .about-panel__heading {
    height: 56px; background: var(--red-dark);
    font-weight: 700; font-size: 19px;
    display: flex; align-items: center; justify-content: center;
  }
  .about-panel__text {
    margin: 12px 66px 0 76px;
    font-style: italic; font-size: 14.5px; line-height: 19px;
    text-align: justify; text-align-last: center;
  }
  .about-panel__contact {
    position: absolute; left: 0; bottom: 0; width: 100%; height: 109px;
    background: var(--red-deep);
    text-align: center; font-size: 16px; line-height: 21px;
    padding-top: 16px; box-sizing: border-box;
  }
  .about-panel__phone { font-weight: 700; font-size: 22px; line-height: 28px; }
  .return-address, .postage-note {
    position: absolute; top: 108px;
    font-family: "Nunito", sans-serif; font-style: italic;
    font-size: 15px; line-height: 19px; color: var(--red);
  }
  .return-address { left: 408px; }
  .postage-note { left: 630px; width: 140px; text-align: center; }
</style>
</head>
<body>

<section class="postcard postcard--front" aria-label="Postcard front">
  <svg width="790" height="564" viewBox="0 0 790 564">
    <defs>
      <linearGradient id="faded-shelves" x1="0" y1="0" x2="1" y2="0">
        <stop offset="0" stop-color="#e9dfcc"/>
        <stop offset="0.5" stop-color="#f1e8d6"/>
        <stop offset="1" stop-color="#e4dac8"/>
      </linearGradient>
      <linearGradient id="store-strip" x1="0" y1="0" x2="1" y2="0">
        <stop offset="0" stop-color="#6b4a33"/>
        <stop offset="0.3" stop-color="#c9c3b8"/>
        <stop offset="0.7" stop-color="#c44a3a"/>
        <stop offset="1" stop-color="#dfe3e6"/>
      </linearGradient>
      <radialGradient id="aisle-photo" cx="0.5" cy="0.5" r="0.6">
        <stop offset="0" stop-color="#d8d6d2"/>
        <stop offset="1" stop-color="#5b6f8a"/>
      </radialGradient>
    </defs>
    <rect width="790" height="564" fill="var(--cream)"/>
    <rect x="0" y="32" width="790" height="433" fill="url(#faded-shelves)" role="img" aria-label="Faded photo of pharmacy shelving"/>
    <rect x="0" y="0" width="790" height="32" fill="var(--red)"/>
    <rect x="0" y="102" width="790" height="8" fill="var(--red)"/>
    <rect x="0" y="110" width="790" height="288" fill="url(#store-strip)" role="img" aria-label="Photos of finished pharmacy interiors with glass display counters and shelving"/>
    <rect x="0" y="398" width="790" height="8" fill="var(--red)"/>
    <rect x="0" y="465" width="790" height="99" fill="var(--red)"/>
    <circle cx="396" cy="254" r="176" fill="var(--red)"/>
    <circle cx="396" cy="254" r="162" fill="url(#aisle-photo)" role="img" aria-label="Photo of a pharmacy aisle with freestanding gondola shelving"/>
  </svg>
  <div class="brand-title front-title">Brightfield Fixtures &amp; Display Co Inc.</div>
</section>

<section class="postcard postcard--back" aria-label="Postcard back">
  <header class="back-header">
    <div class="brand-title">Brightfield Fixtures &amp; Display Co Inc.</div>
  </header>

  <div class="about-panel">
    <div class="about-panel__heading">Quality - Experience - Innovation</div>
    <p class="about-panel__text">Family owned and operated fo three generations Brightfield Fixtures &amp; Display Co. Inc is the oldest store fixture company in New Jersey. As designers &amp; Manufacturers we can save you hours of time and money. Our level of experience will be evident from the outset and you will be pleased that you found us.</p>
    <div class="about-panel__contact">
      <div class="about-panel__phone">201 555 0148</div>
      <div>display@brightfieldfixtures.com</div>
      <div>www.brightfieldfixtures.com</div>
    </div>
  </div>

  <address class="return-address">Brightfield<br>Fixtures &amp;<br>Display Co.<br>PO Box 318<br>Ridgefield<br>NJ 07657</address>

  <div class="postage-note">Presorted<br>First Class US<br>POSTAGE OAID<br>Postway</div>

  <footer class="back-footer"></footer>
</section>

</body>
</html>
```